K.T.L Electrical Services Pty Ltd

Electrical contracting business. I have a base for the design which i like. The contact number needs to be changed to 0491637204 and the O made more solid and level with the rest of the letters. If you have any other ideas of what would make it better I'm happy to see them.

The back side to be written as dot points with the following:
- Residential & Commercial
- Maintenance
- PV & Battery servicing
- EV Chargers

```html
<!DOCTYPE html>
<html lang="en">
<head>
<meta charset="utf-8">
<title>K.T.L Electrical Services – Business Cards</title>
<link rel="stylesheet" href="https://fonts.googleapis.com/css2?family=Questrial&family=Roboto:wght@500;700&display=swap">
<style>
  :root {
    --stage: #1c4fc0;
    --card-blue: #0a75bb;
    --card-black: #0a0606;
    --brand-blue: #0b79c6;
    --grey: #8a8a8a;
    --white: #ffffff;
  }
  * { box-sizing: border-box; margin: 0; padding: 0; }
  html, body { width: 1200px; height: 900px; overflow: hidden; }
  body {
    background: var(--stage);
    font-family: "Questrial", "Century Gothic", sans-serif;
    position: relative;
  }
  .card {
    position: absolute;
    width: 560px;
    height: 320px;
    border-radius: 34px;
    box-shadow: 0 10px 28px rgba(0, 0, 0, 0.28);
    overflow: hidden;
  }

  /* Back card */
  .card--back { left: 80px; top: 110px; background: var(--card-blue); color: var(--white); }
  .phone {
    position: absolute; left: 44px; top: 40px;
    display: flex; align-items: center; gap: 10px;
    font-size: 21px; letter-spacing: 0.5px;
  }
  .phone svg { width: 18px; height: 18px; fill: var(--white); }
  .brand-small {
    position: absolute; right: 44px; top: 88px;
    text-align: center; font-family: "Roboto", sans-serif;
  }
  .brand-small .brand-row { display: flex; align-items: center; justify-content: center; gap: 8px; }
  .brand-small .brand-dot { width: 30px; height: 30px; border-radius: 50%; background: var(--white); }
  .brand-small .brand-name { font-size: 46px; font-weight: 500; line-height: 1; }
  .brand-small .brand-sub { font-size: 12px; font-weight: 500; letter-spacing: 1.5px; margin-top: 2px; }
  .brand-small .brand-licence { font-size: 9px; letter-spacing: 1.2px; }

  .services-title {
    position: absolute; left: 44px; top: 170px;
    font-weight: 700; font-family: "Roboto", sans-serif;
    font-size: 16px; letter-spacing: 0.3px;
  }
  .service-list { list-style: none; position: absolute; font-size: 20px; line-height: 1.3; }
  .service-list li::before { content: "•"; margin-right: 12px; }
  .service-list--left { left: 44px; top: 198px; }
  .service-list--right { left: 300px; top: 236px; }
  .divider { position: absolute; left: 290px; top: 220px; width: 226px; height: 1px; background: var(--white); }

  /* Front card */
  .card--front { left: 560px; top: 470px; background: var(--card-black); }
  .brand-large {
    position: absolute; left: 0; right: 0; top: 40px;
    text-align: center; font-family: "Roboto", sans-serif;
  }
  .brand-large .brand-row { display: flex; align-items: center; justify-content: center; gap: 16px; }
  .brand-large .brand-dot { width: 92px; height: 92px; border-radius: 50%; background: var(--brand-blue); }
  .brand-large .brand-name { font-size: 112px; font-weight: 500; color: var(--brand-blue); line-height: 1; }
  .brand-large .brand-sub {
    font-size: 30px; font-weight: 700; color: var(--grey);
    letter-spacing: 3px; margin-top: 4px;
  }
  .licence-row {
    display: flex; align-items: center; justify-content: center; gap: 16px; margin-top: 6px;
  }
  .licence-row .rule { width: 100px; height: 3px; background: var(--grey); }
  .licence-row .brand-licence { font-size: 24px; font-weight: 500; color: var(--brand-blue); letter-spacing: 2px; }
  .tagline {
    position: absolute; left: 0; right: 0; bottom: 34px;
    text-align: center; color: var(--brand-blue);
    font-size: 16px; letter-spacing: 3px; text-transform: uppercase;
  }
</style>
</head>
<body>

  <section class="card card--back">
    <div class="phone">
      <svg viewBox="0 0 24 24" aria-hidden="true"><path d="M6.6 10.8a15.1 15.1 0 0 0 6.6 6.6l2.2-2.2a1 1 0 0 1 1-.25 11.4 11.4 0 0 0 3.6.57 1 1 0 0 1 1 1V20a1 1 0 0 1-1 1A17 17 0 0 1 3 4a1 1 0 0 1 1-1h3.5a1 1 0 0 1 1 1c0 1.25.2 2.45.57 3.57a1 1 0 0 1-.25 1z"/></svg>
      <span>0-491-637-204</span>
    </div>

    <div class="brand-small">
      <div class="brand-row">
        <span class="brand-dot"></span>
        <span class="brand-name">K.T.L</span>
      </div>
      <div class="brand-sub">ELECTRICAL SERVICES P/L</div>
      <div class="brand-licence">EC 20417</div>
    </div>

    <h2 class="services-title">FACILITY SERVICES OFFERED</h2>
    <ul class="service-list service-list--left">
      <li>Residential &amp; Commercial</li>
      <li>Maintenance</li>
    </ul>
    <div class="divider"></div>
    <ul class="service-list service-list--right">
      <li>PV &amp; Battery servicing</li>
      <li>EV Chargers</li>
    </ul>
  </section>

  <section class="card card--front">
    <div class="brand-large">
      <div class="brand-row">
        <span class="brand-dot"></span>
        <span class="brand-name">K.T.L</span>
      </div>
      <div class="brand-sub">ELECTRICAL SERVICES P/L</div>
      <div class="licence-row">
        <span class="rule"></span>
        <span class="brand-licence">EC 20417</span>
        <span class="rule"></span>
      </div>
    </div>
    <p class="tagline">Australian company operating West Australia</p>
  </section>

</body>
</html>
```